Electrical business needs a flyer design

we need a Trifold flyer designed for an electrical company. Our service include new installations, renovations and rewires, safety checks, switchboard upgrades, services and breakdown, home automation and power monitoring. we would like to see designs using dark grey, orange and blue. the final designs should communicate a friendly but professional service. I have attached my old business brochure to indicate the service we provide
Target Market(s)
home owners
Industry/Entity Type
Electrical
Look and feel
Each slider illustrates characteristics of the customer's brand and the style your logo design should communicate.

```html
<!DOCTYPE html>
<html lang="en">
<head>
<meta charset="utf-8">
<title>Kestrel Electrical – Trifold Flyer</title>
<link href="https://fonts.googleapis.com/css2?family=Montserrat:wght@500;600;700;800&family=Roboto:wght@400;500&display=swap" rel="stylesheet">
<style>
  :root{
    --orange:#f07122;
    --blue:#1a8fd6;
    --ink:#2b2b2b;
    --mist:#eef0f0;
    --paper:#ffffff;
    --stage:#f6f6f6;
    --ember-dark:#2a0d02;
    --ember:#a8400f;
  }
  *{margin:0;padding:0;box-sizing:border-box}
  html,body{width:1200px;height:947px;overflow:hidden;background:var(--stage)}
  body{position:relative;font-family:"Roboto",Arial,sans-serif;color:var(--ink)}
  .sheet{position:absolute;background:var(--paper);overflow:hidden}
  .sheet > svg.backdrop{position:absolute;left:0;top:0}
  .abs{position:absolute}
  .head{font-family:"Montserrat",Arial,sans-serif;font-weight:700;line-height:1}
  .orange{color:var(--orange)}
  .blue{color:var(--blue)}
  .brand{display:flex;align-items:center;gap:6px;font-family:"Montserrat",Arial,sans-serif;font-weight:700;color:var(--blue);white-space:nowrap}
  .brand .dot{border-radius:50%;background:var(--blue);flex:none}
  .small{font-size:4.8px;line-height:1.55;font-weight:500}
  .tiny{font-size:4.2px;line-height:1.5;font-weight:500}
  .rule{position:absolute;background:var(--orange)}
  .ticks{list-style:none;position:absolute}
  .ticks li{position:relative;padding-left:21px;font-family:"Montserrat",Arial,sans-serif;font-weight:500;font-size:10.5px;line-height:1.2;margin-bottom:8px}
  .ticks li::before{content:"";position:absolute;left:0;top:2px;width:10px;height:10px;border-radius:50%;background:var(--blue)}
  .contact{font-size:7.6px;line-height:1.45}
  .contact b{font-weight:400;color:var(--blue)}
  .book{position:absolute;border:1.2px solid var(--blue);border-radius:10px;font-family:"Montserrat",Arial,sans-serif;font-weight:600;font-size:7.5px;display:flex;align-items:center;justify-content:center;gap:10px;background:var(--paper)}
</style>
</head>
<body>

<!-- Front cover -->
<section class="sheet cover" style="left:102px;top:86px;width:369px;height:789px">
  <svg class="backdrop" width="369" height="789" viewBox="0 0 369 789">
    <path d="M0 0H369V60C350 250 260 300 215 215C150 330 80 330 0 358Z" fill="var(--mist)"/>
    <path d="M369 590C330 700 250 700 175 789H369Z" fill="var(--orange)"/>
    <circle cx="190" cy="351" r="159" fill="var(--mist)"/>
    <defs><radialGradient id="emberA" cx="50%" cy="50%" r="55%"><stop offset="0" stop-color="#e2661c"/><stop offset=".55" stop-color="var(--ember)"/><stop offset="1" stop-color="var(--ember-dark)"/></radialGradient></defs>
    <circle cx="190" cy="351" r="141" fill="url(#emberA)" role="img" aria-label="Glowing orange lightning bolt artwork"/>
  </svg>
  <div class="brand abs" style="left:70px;top:86px;font-size:21px"><span class="dot" style="width:16px;height:16px"></span>Kestrel Electrical</div>
  <div class="head abs" style="left:33px;top:563px;font-size:33px">For all your</div>
  <div class="head abs orange" style="left:33px;top:602px;font-size:52px;line-height:.98">Electrical<br>needs</div>
  <div class="rule" style="left:32px;top:713px;width:52px;height:4px"></div>
</section>

<!-- Outside spread -->
<section class="sheet spread-outer" style="left:577px;top:86px;width:544px;height:389px">
  <svg class="backdrop" width="544" height="389" viewBox="0 0 544 389">
    <rect x="181" width="182" height="389" fill="var(--mist)"/>
    <path d="M0 0H181V389H0Z" fill="var(--paper)"/>
    <path d="M0 150C60 110 130 120 181 180V0H0Z" fill="var(--mist)"/>
    <path d="M181 180C230 240 290 220 363 165V389H181Z" fill="var(--paper)"/>
    <path d="M0 0H147C147 80 80 147 0 147Z" fill="#8a9096" role="img" aria-label="Photo of an electrician wiring a switchboard"/>
    <path d="M363 0H544V389H363Z" fill="var(--paper)"/>
    <path d="M363 0H544V40C520 200 420 120 363 200Z" fill="var(--mist)"/>
    <path d="M544 291C530 350 480 350 448 389H544Z" fill="var(--orange)"/>
    <circle cx="457" cy="173" r="78" fill="var(--mist)"/>
    <defs><radialGradient id="emberB" cx="50%" cy="50%" r="55%"><stop offset="0" stop-color="#e2661c"/><stop offset=".55" stop-color="var(--ember)"/><stop offset="1" stop-color="var(--ember-dark)"/></radialGradient></defs>
    <circle cx="457" cy="173" r="69" fill="url(#emberB)" role="img" aria-label="Glowing orange lightning bolt artwork"/>
    <circle cx="267" cy="201" r="40" fill="#d6ebf8" role="img" aria-label="Blue icon of a fist gripping a lightning bolt"/>
  </svg>

  <p class="small abs" style="left:20px;top:166px;width:136px">We offer a 24-hour, seven-day emergency response service where you need an electrician due to a breakdown or other disruption to your power supply. Our electrical contractors will identify the fault and have your power back on as soon as possible.</p>
  <div class="head abs" style="left:20px;top:225px;font-size:13px;font-weight:600">Accredited master</div>
  <div class="head abs orange" style="left:20px;top:243px;font-size:19px">ELECTRICIAN</div>
  <ul class="abs" style="left:20px;top:276px;width:140px;list-style:none">
    <li class="tiny" style="position:relative;padding-left:21px;height:36px"><span class="abs" style="left:0;top:1px;width:10px;height:10px;border-radius:50%;background:var(--blue)"></span>Electrical work is one of the most dangerous tasks that can be performed in a home or business. Every year, dozens of people are electrocuted or shocked by substandard electrical work.</li>
    <li class="tiny" style="position:relative;padding-left:21px;height:28px"><span class="abs" style="left:0;top:1px;width:10px;height:10px;border-radius:50%;background:var(--blue)"></span>By choosing a Master Electrician, you are choosing a contractor whose safety systems are accredited and monitored, and who provides a workmanship guarantee.</li>
    <li class="tiny" style="position:relative;padding-left:21px"><span class="abs" style="left:0;top:1px;width:10px;height:10px;border-radius:50%;background:var(--blue)"></span>Master Electricians are reliable contractors who provide excellent services and information, potentially saving you time and money.</li>
  </ul>

  <div class="head abs orange" style="left:199px;top:26px;font-size:19px">About us</div>
  <p class="small abs" style="left:200px;top:49px;width:150px">Kestrel is a privately owned business providing a comprehensive range of domestic, commercial and industrial electrical services.<br><br>We provide a comprehensive range of electrical and communication services including small jobs around the home to large industrial applications. Our business is underpinned by a commitment to customer service, that is, we turn up on time providing quality workmanship at a fair and competitive price.</p>
  <div class="head abs" style="left:202px;top:289px;font-size:13px;font-weight:500"><span class="blue">Get in</span> touch now :</div>
  <div class="abs" style="left:202px;top:306px;width:24px;height:1.5px;background:var(--blue)"></div>
  <div class="contact abs" style="left:202px;top:314px;width:150px">
    <div><b>Phone :</b> 0400 555 012 &nbsp;<b>Fax :</b> 8555 0199</div>
    <div><b>E-mail :</b> hello@kestrelelectrical.example</div>
    <div><b>Address :</b> PO Box 418 Riverton<br><span style="padding-left:35px">SA 5999</span></div>
  </div>

  <div class="brand abs" style="left:392px;top:46px;font-size:11px;gap:4px"><span class="dot" style="width:9px;height:9px"></span>Kestrel Electrical</div>
  <div class="head abs" style="left:380px;top:278px;font-size:16px;font-weight:600">For all your</div>
  <div class="head abs orange" style="left:380px;top:296px;font-size:25px;line-height:1">Electrical<br>needs</div>
  <div class="rule" style="left:380px;top:351px;width:25px;height:2px"></div>
</section>

<!-- Inside spread -->
<section class="sheet spread-inner" style="left:576px;top:495px;width:545px;height:389px">
  <svg class="backdrop" width="545" height="389" viewBox="0 0 545 389">
    <rect x="182" width="182" height="389" fill="#fafafa"/>
    <path d="M0 253C70 245 115 290 136 330V389H0Z" fill="var(--orange)"/>
    <path d="M545 270C470 270 410 330 385 389H545Z" fill="var(--mist)"/>
    <path d="M380 0H545V165C470 170 380 110 380 0Z" fill="#8a8f95" role="img" aria-label="Photo of an electrician testing a switchboard with a multimeter"/>
    <circle cx="50" cy="333" r="35" fill="#c9ccce" role="img" aria-label="Photo of phone and data wall sockets"/>
    <circle cx="131" cy="333" r="35" fill="#e4e4e2" role="img" aria-label="Photo of a plug going into a wall outlet"/>
    <circle cx="233" cy="333" r="35" fill="#b9a48e" role="img" aria-label="Photo of safety switches in a switchboard"/>
    <circle cx="314" cy="333" r="35" fill="#b06a35" role="img" aria-label="Photo of hands stripping a wire"/>
  </svg>

  <div class="head abs orange" style="left:14px;top:26px;font-size:16px">Communication</div>
  <div class="head abs" style="left:14px;top:46px;font-size:16px;font-weight:600">Services</div>
  <p class="small abs" style="left:14px;top:73px;width:140px">Lorem ipsum dolor sit amet, consectetuer adipiscing elit, sed diam nonummy nibh euismod tincidunt ut laoreet dolore magna aliquam erat volutpat. Ut wisi enim ad minim veniam, quis nostrud exerci tation ullamcorper suscipit lobortis nisl ut aliquip ex ea commodo consequat.</p>
  <ul class="ticks" style="left:14px;top:136px;width:150px">
    <li>new installations</li>
    <li>additional phone and data points</li>
    <li>antennas and TV points</li>
    <li>IAN setups</li>
  </ul>

  <div class="head abs orange" style="left:197px;top:26px;font-size:16px">Electronic</div>
  <div class="head abs" style="left:197px;top:46px;font-size:16px;font-weight:600">Services</div>
  <p class="small abs" style="left:197px;top:73px;width:140px">Lorem ipsum dolor sit amet, consectetuer adipiscing elit, sed diam nonummy nibh euismod tincidunt ut laoreet dolore magna aliquam erat volutpat. Ut wisi enim ad minim veniam, quis nostrud exerci tation ullamcorper suscipit lobortis nisl ut aliquip ex ea commodo consequat.</p>
  <ul class="ticks" style="left:197px;top:136px;width:135px">
    <li>new installations</li>
    <li>renovations and re-wiring</li>
    <li>installation of safety switches</li>
    <li>switchboard upgrades</li>
    <li>services and break downs</li>
  </ul>

  <div class="head abs orange" style="left:378px;top:159px;font-size:19px">Our</div>
  <div class="head abs" style="left:378px;top:181px;font-size:19px;font-weight:600">Philosophy</div>
  <p class="small abs" style="left:378px;top:212px;width:155px">Kestrel Electrical focuses on providing our customers with the best possible service available. Our trades people are highly qualified to ensure quality and reliability. We strive to continually change and grow within the industry. We are constantly making changes to serve you better.</p>
  <div class="book" style="left:383px;top:312px;width:90px;height:20px">BOOK NOW <span class="blue">›</span></div>
  <div class="head abs blue" style="left:379px;top:338px;font-size:22px">0400 555 012</div>
</section>

</body>
</html>
```